San Francisco Leading Consulting firm - Quorvane Web Design Project

•Create a Web Design
•Uncoded webpage layout design
•2 Pages Design - Homepage + Interior Page

Task Description
Hello, we're looking for a re-design our current website www.quorvane-example.com

we have a sample mockup design @

http://quorvane.pubmirrex-example.org/

This shows the layout that we like and also a sample of 6 pictures that would change based on where you mouse over..

6 pictures HOME design needs to be included.

SMART
THOUGHTFUL
FLEXIBLE
CREATIVE SERVICES
TECHNICAL SERVICES
PARTNERS

sites we like:

http://www.belvantoadvisory-example.com/Home.cfm?id=Home
http://www.plumstudioworks-example.com/index.html

Our company can be best described as: 100+ employees, cutting-edge, depandable, innovative, strong, smart.

Our Primary focus is: IT Consulting Services and Creative Design services

Quorvane LLC is a consulting firm providing creative design, business and technology solutions to both private and public interests.

Established in 1996, Quorvane is a San Francisco based company providing specialists for a range of business needs including:

Creative Design Services
•Print
•Logo Design
•Website Design
•Illustration

and

Business and Technology solutions

•Application Software and Web Development
•Business Process Re-Design (BPR)
•Business/Systems Analysis and Requirement Documentation
•Mentoring and Training
•Network/Hardware Installation Services
•System Design and Architecture
•Vendor Management
•Sharepoint Architecture and Implementation

our sample mockup site:

Reason: Due to holiday season, we're not available to work with designers and finilize our design.  

Thank you very much for submitting your design.

We appreciate your time and creativity.   Since, our office is currently closed for holidays, we will be reviewing it in details next week and will make our decision as soon as possible.

It would be great if you could submit any of your changes by Wed next week, so it would be part of our reviews. 

Please see updated wireframe under attachments:  we have some minor updates to our wireframe that we would like you to update your designs, if possible.  

We also encorouge you not to use our standard wireframe and come up with more unique designs.   Everything would be considered when we review your design.

 

Target Market(s)

Creative services and professional services clients, including government agencies

Industry/Entity Type

Business

Requirements
Must have
• Clean, professional look, easy navigation

```html
<!DOCTYPE html>
<html lang="en">
<head>
<meta charset="utf-8">
<title>Quorvane – Home</title>
<link rel="stylesheet" href="https://fonts.googleapis.com/css2?family=Open+Sans:wght@400;600;700&family=Tinos:wght@400;700&display=swap">
<style>
  :root {
    --frame: #8fb0d6;
    --page: #d9dadc;
    --page-light: #eeeff0;
    --navy: #2b3566;
    --navy-dark: #1c2350;
    --nav-text: #dfe6ff;
    --accent-red: #c0282d;
    --ink-blue: #4b84be;
    --logo-blue: #3a8fd6;
    --logo-gray: #7b7e82;
    --hero-black: #050505;
    --hero-orange: #f07d14;
    --tile-blue: #1d3f82;
    --rule: #9a9ca0;
    --footer: #000;
    --white: #fff;
  }
  * { box-sizing: border-box; margin: 0; padding: 0; }
  html, body { width: 983px; height: 1200px; overflow: hidden; }
  body {
    position: relative;
    background: var(--frame);
    font-family: "Tinos", "Times New Roman", serif;
  }
  .page {
    position: absolute; left: 13px; top: 13px; width: 957px; height: 1187px;
    background:
      radial-gradient(ellipse 520px 420px at 560px 640px, rgba(255,255,255,.55), rgba(255,255,255,0) 70%),
      linear-gradient(180deg, var(--page-light) 0%, var(--page) 40%, var(--page) 100%);
    overflow: hidden;
  }
  /* Header */
  .masthead { position: absolute; left: 0; top: 0; width: 957px; height: 172px; }
  .brand { position: absolute; left: 50px; top: 70px; display: flex; align-items: center; gap: 18px; }
  .brand-dot { width: 54px; height: 54px; border-radius: 50%; background: var(--logo-blue); }
  .brand-name {
    font-family: "Open Sans", sans-serif; font-weight: 400; font-size: 62px;
    color: var(--logo-gray); letter-spacing: 1px; line-height: 1;
  }
  /* Navigation */
  .main-nav {
    position: absolute; left: 0; top: 176px; width: 957px; height: 22px;
    background: linear-gradient(180deg, var(--navy) 0%, var(--navy-dark) 100%);
    display: flex; align-items: center; padding-left: 10px;
  }
  .main-nav a {
    font-family: "Open Sans", sans-serif; font-weight: 700; font-size: 10px;
    color: var(--nav-text); text-decoration: none; text-transform: uppercase;
    padding: 0 12px; height: 22px; line-height: 22px;
  }
  .main-nav a.is-current {
    background: var(--white); color: var(--accent-red); width: 90px; text-align: center; margin-right: 14px;
  }
  .contact-line {
    position: absolute; left: 16px; top: 208px;
    font-family: "Open Sans", sans-serif; font-size: 8.5px; color: var(--navy);
  }
  /* Hero */
  .hero {
    position: absolute; left: 0; top: 223px; width: 957px; height: 282px;
    background: var(--hero-black); border-radius: 16px; border: 2px solid #ccc;
  }
  .hero-photo {
    position: absolute; left: 20px; top: 10px; width: 915px; height: 220px;
    background:
      radial-gradient(ellipse 170px 120px at 78% 28%, rgba(226,200,180,.55), rgba(226,200,180,0) 70%),
      radial-gradient(ellipse 420px 200px at 62% 50%, rgba(150,150,150,.55), rgba(150,150,150,0) 75%),
      radial-gradient(ellipse 260px 160px at 18% 70%, rgba(110,110,110,.45), rgba(110,110,110,0) 75%),
      linear-gradient(180deg, #3a3a3a 0%, #1d1d1d 100%);
  }
  .hero-note { position: absolute; right: 30px; top: 12px; font-size: 9px; color: var(--hero-orange); }
  .hero-title {
    position: absolute; left: 42px; top: 46px;
    font-family: "Open Sans", sans-serif; font-weight: 700; font-size: 66px; color: var(--hero-orange); line-height: 1;
  }
  .hero-tagline {
    position: absolute; left: 222px; top: 145px;
    font-family: "Open Sans", sans-serif; font-size: 19px; color: var(--hero-orange);
  }
  .hero-motto {
    position: absolute; left: 0; top: 250px; width: 100%; text-align: center;
    font-size: 14px; color: var(--white);
  }
  /* Audience tiles */
  .audiences { position: absolute; left: 0; top: 525px; width: 957px; height: 180px; }
  .audience { position: absolute; top: 0; width: 184px; }
  .audience-photo { height: 162px; border-radius: 14px 14px 0 0; }
  .audience-photo--building {
    background: radial-gradient(ellipse 62px 70px at 50% 58%, #8d96a6 0%, #4a5872 40%, #141c2c 75%, #020308 100%);
  }
  .audience-photo--tower {
    background: radial-gradient(ellipse 60px 72px at 50% 55%, #7f8ea5 0%, #3f5170 42%, #121a2b 75%, #020308 100%);
  }
  .audience-photo--handshake {
    background:
      radial-gradient(ellipse 48px 24px at 50% 56%, rgba(200,170,150,.75), rgba(200,170,150,0) 80%),
      radial-gradient(ellipse 70px 70px at 50% 55%, #5c7fb0 0%, #26406a 45%, #0b1322 78%, #020308 100%);
  }
  .audience-label {
    height: 16px; background: linear-gradient(180deg, #fff, #cfd3da);
    font-family: "Open Sans", sans-serif; font-weight: 700; font-size: 11px;
    color: var(--tile-blue); text-align: center; line-height: 16px; text-transform: uppercase;
  }
  .rule { position: absolute; left: 0; top: 709px; width: 957px; height: 2px; background: var(--rule); }
  /* Intro */
  .intro { position: absolute; left: 0; top: 716px; width: 945px; color: var(--ink-blue); }
  .intro h2 { font-size: 14px; font-weight: 700; }
  .intro ul { list-style: disc; padding-left: 54px; margin-top: 18px; }
  .intro li { font-size: 12.5px; line-height: 1.35; }
  /* Services */
  .services-heading {
    position: absolute; left: 0; top: 942px; font-size: 17px; font-weight: 700; color: var(--ink-blue);
  }
  .service-list {
    position: absolute; top: 1008px; list-style: disc; color: var(--ink-blue); font-size: 14px; line-height: 1.4;
  }
  /* Footer */
  .site-footer {
    position: absolute; left: 0; top: 1157px; width: 957px; height: 30px; background: var(--footer);
    color: var(--white); text-align: center; font-size: 14px; line-height: 26px;
  }
</style>
</head>
<body>
<div class="page">
  <header class="masthead">
    <div class="brand"><span class="brand-dot"></span><span class="brand-name">Quorvane</span></div>
  </header>

  <nav class="main-nav">
    <a class="is-current" href="#">Home</a>
    <a href="#">Company</a>
    <a href="#">Technical Services</a>
    <a href="#">Creative Services</a>
    <a href="#">Partners</a>
    <a href="#">Contact Us</a>
  </nav>
  <p class="contact-line">Quorvane - San Francisco / &nbsp;Phone: 1-415-555-0140 / &nbsp;Fax: 1-415-555-0145 /</p>

  <section class="hero">
    <div class="hero-photo" role="img" aria-label="Photograph of a hand writing mathematical formulas with chalk on a blackboard"></div>
    <p class="hero-note">["carousel" slide show that features high-quality photographs and text that highlights Quorvane brand attributes]</p>
    <h1 class="hero-title">smart:</h1>
    <p class="hero-tagline">we don’t believe in the term “overqualified”</p>
    <p class="hero-motto">Our Business Is Your Business</p>
  </section>

  <section class="audiences">
    <div class="audience" style="left:96px">
      <div class="audience-photo audience-photo--building" role="img" aria-label="Photograph of a classical building facade"></div>
      <div class="audience-label">For Graphic Designers</div>
    </div>
    <div class="audience" style="left:378px">
      <div class="audience-photo audience-photo--tower" role="img" aria-label="Photograph of an office tower seen from below"></div>
      <div class="audience-label">For Clients</div>
    </div>
    <div class="audience" style="left:659px">
      <div class="audience-photo audience-photo--handshake" role="img" aria-label="Photograph of a business handshake"></div>
      <div class="audience-label">For Partners</div>
    </div>
  </section>

  <div class="rule"></div>

  <section class="intro">
    <h2>Quorvane</h2>
    <ul>
      <li>Quorvane provides professional experience in all phases of IT projects from vendor selection to post production support. We assist our clients not only in their IT solutions, but also provide professional services such as transitioning with conversion activities, Business Process Reengineering (BPR), training and business support. We have provided vendor analysis and selection, project oversight, architecture, requirements gathering and system certification functions.</li>
    </ul>
  </section>

  <h2 class="services-heading">Our corporate consulting services include a wide array of talent and expertise in the following:</h2>
  <ul class="service-list" style="left:46px">
    <li>Process Redesign</li>
    <li>Production Support</li>
    <li>SQL</li>
    <li>Process Redesign</li>
  </ul>
  <ul class="service-list" style="left:253px;width:160px">
    <li>System Design and Architecture</li>
    <li>Vendor Management</li>
    <li>Analysis</li>
    <li>Business Intelligence</li>
    <li>CRM</li>
  </ul>
  <ul class="service-list" style="left:461px">
    <li>Network/Hardware Installation Services</li>
    <li>Project Management</li>
  </ul>

  <footer class="site-footer">Copyright 2010, Quorvane, LLC All rights reserved.</footer>
</div>
</body>
</html>
```